依頼詳細
・当社で建築した物件とイメージキャラクターをデザインに盛り込んだ提案をお願いします。(添付ファイル有)
・封筒の色は白で考えています。
・封筒サイズ:角2、角0(角2と同じデザイン)、長3(縦向き)
記載項目
・会社ロゴ ・会社マーク ※添付ファイル有
〒245-0623
神奈川県横浜市戸塚区下柏尾町517-4 リベルタ北園3F
TEL 045-770-2914(代表)
045-770-2957(工事部)
045-770-2986(不動産部)
FAX 045-770-2938
www.hinorisa-corp.com
E-mail info@hinorisa-corp.com
・当社で建築した物件(添付ファイル写真)のいずれかを背景等に使って下さい。
・イメージキャラクター ヒノリくん(添付ファイル有)
希望イメージ
• +5 0 +5
• シンプル
複雑
• 単色
カラフル
• 暗い
明るい
• 日常
高級
• 遊び心
厳粛
• 未来的
伝統的
• 女性的
男性的
希望する色
緑系、黄・オレンジ系、物件写真はモノクロやセピア調に加工して頂いてもかまいません。
納品ファイル
• 高解像度JPG (.jpg)
補足説明
当社の名刺も添付します。
3段目、4段目のような雰囲気をイメージして頂くといいかと思います。
依頼公開後の追記内容
■ 選んだ理由

色使いや配置が細部にわたりバランス良く、綺麗にまとまっていました。
重要な書類の送付にも問題なく、また社員投票でも一番人気だったので選ばせて頂きました。

■ 提案者全員のお礼・コメント

ランサーの皆さま、この度は当社の会社封筒デザインにたくさんの素敵なご提案を頂きましてありがとうございます。

皆さまの作品のコメントを拝見すると、どれも「なるほど!」と思うものばかりで、一点を選ぶのに大変苦労しました。

また何かご縁がありました際にはよろしくお願い致します。

```html
<!DOCTYPE html>
<html lang="ja">
<head>
<meta charset="UTF-8">
<title>ヒノリサコーポレーション 封筒デザイン</title>
<link rel="stylesheet" href="https://fonts.googleapis.com/css2?family=Noto+Sans+JP:wght@400;500;700;900&display=swap">
<style>
  :root {
    --green: #3fae3a;
    --orange: #f29418;
    --sepia-light: #e6c89a;
    --sepia-mid: #b98a52;
    --sepia-dark: #6e4a26;
    --ink: #1a1a1a;
    --accent-red: #d9231d;
    --paper: #ffffff;
    --box-line: #222222;
  }
  * { margin: 0; padding: 0; box-sizing: border-box; }
  html, body { width: 802px; height: 1200px; overflow: hidden; background: var(--paper); }
  body { font-family: "Noto Sans JP", sans-serif; color: var(--ink); }

  .envelope { position: relative; width: 802px; height: 1200px; overflow: hidden; background: var(--paper); }

  .flap { position: absolute; left: 0; top: 0; width: 802px; height: 52px; background: var(--green); }

  .postal-boxes { position: absolute; left: 468px; top: 174px; display: flex; align-items: center; gap: 4px; }
  .postal-box { width: 29px; height: 33px; border: 2px solid var(--box-line); }
  .postal-dash { width: 10px; height: 2px; background: var(--box-line); margin: 0 1px; }

  .sun { position: absolute; left: 400px; top: 600px; width: 420px; height: 420px; border-radius: 50%; background: var(--orange); }

  .building-photo {
    position: absolute; left: 250px; top: 690px; width: 552px; height: 430px;
    background:
      linear-gradient(90deg, rgba(255,255,255,1) 0%, rgba(255,255,255,0) 35%),
      linear-gradient(160deg, var(--sepia-light) 0%, var(--sepia-mid) 50%, var(--sepia-dark) 100%);
  }

  .layer { position: absolute; left: 0; top: 0; width: 802px; height: 1200px; }

  .web-vertical {
    position: absolute; left: 17px; top: 1180px;
    transform: rotate(-90deg); transform-origin: left top;
    font-size: 14px; font-weight: 500; color: var(--paper); letter-spacing: 0.04em; white-space: nowrap;
  }

  .company-block { position: absolute; left: 78px; top: 995px; }
  .brand-name { font-size: 22px; font-weight: 700; color: var(--ink); letter-spacing: 0.08em; line-height: 1; }
  .company-name { margin-top: 10px; font-size: 30px; font-weight: 900; color: var(--ink); letter-spacing: 0.02em; line-height: 1; white-space: nowrap; }

  .contact { position: absolute; left: 78px; top: 1096px; font-size: 12px; line-height: 1.45; color: var(--ink); white-space: nowrap; }
  .contact .tel-main { color: var(--accent-red); font-weight: 700; font-size: 17px; }
  .contact .tel-label { color: var(--accent-red); font-weight: 700; }
  .contact .note { font-size: 9px; }

  .mascot { position: absolute; left: 660px; top: 990px; width: 110px; height: 190px; border-radius: 46px 46px 20px 20px;
    background: linear-gradient(180deg, #f2c84a 0%, #e2a93a 60%, #c98a2c 100%); }
</style>
</head>
<body>
<div class="envelope">

  <div class="flap"></div>

  <div class="postal-boxes">
    <div class="postal-box"></div>
    <div class="postal-box"></div>
    <div class="postal-box"></div>
    <div class="postal-dash"></div>
    <div class="postal-box"></div>
    <div class="postal-box"></div>
    <div class="postal-box"></div>
    <div class="postal-box"></div>
  </div>

  <div class="sun"></div>

  <div class="building-photo" role="img" aria-label="当社で建築した物件の外観写真（セピア調）"></div>

  <svg class="layer info-panel" viewBox="0 0 802 1200" aria-hidden="true">
    <polygon points="40,1030 640,950 640,1200 40,1200" fill="var(--paper)"/>
  </svg>

  <svg class="layer side-band" viewBox="0 0 802 1200" aria-hidden="true">
    <polygon points="0,790 52,770 52,1200 0,1200" fill="var(--green)"/>
  </svg>
  <div class="web-vertical">www.hinorisa-corp.com</div>

  <div class="company-block">
    <div class="brand-name">HINORISA</div>
    <div class="company-name">株式会社 ヒノリサコーポレーション</div>
  </div>

  <div class="contact">
    <div>〒245-0623　神奈川県横浜市戸塚区下柏尾町517-4 リベルタ北園3F</div>
    <div><span class="tel-label">TEL.</span> <span class="tel-main">045-770-2914</span><span class="note">(代表)</span>　045-770-2957<span class="note">(工事部)</span>　045-770-2986<span class="note">(不動産部)</span></div>
    <div>FAX : 045-770-2938　　E-mail : info@hinorisa-corp.com</div>
  </div>

  <div class="mascot" role="img" aria-label="イメージキャラクター ヒノリくん"></div>

</div>
</body>
</html>
```